Willowmere Loft B&B Business Card

This beautiful high-class B&B is looking for a business card that stands out from the rest. They are in the middle of the countryside, have chickens, geese and a dog. They also love bumble bees.

I was maybe thinking a rustic drawing / print of a bumble bee and a sketch of the house, I am not sure.. I quite like the feel of this... http://www.tarnwick-mill.co.uk/

Industry/Entity Type

Business

Contact Information for Business Card

Willowmere Loft
Bed & Breakfast
Brackleford, Hensworth, Somerset, TA14 7QP
01632 960418 | www.willowmereloft.co.uk

```html
<!DOCTYPE html>
<html lang="en">
<head>
<meta charset="utf-8">
<title>Willowmere Loft B&amp;B Business Card</title>
<link href="https://fonts.googleapis.com/css2?family=Didact+Gothic&family=Open+Sans:wght@400;700&family=Cinzel&display=swap" rel="stylesheet">
<style>
  :root {
    --page-bg: #e9e7e4;
    --card-white: #fbfbfb;
    --brand-blue: #1b9ae6;
    --text-dark: #2b2b2b;
    --text-grey: #8a8a8a;
    --photo-sky: #6fa4dc;
    --photo-stone: #c9b58a;
    --photo-grass: #5f8a3c;
  }
  * { margin: 0; padding: 0; box-sizing: border-box; }
  html, body { width: 1200px; height: 844px; overflow: hidden; }
  body {
    background: var(--page-bg);
    position: relative;
    font-family: "Open Sans", sans-serif;
  }
  .card {
    position: absolute;
    top: 273px;
    width: 520px;
    height: 298px;
    box-shadow: 0 6px 18px rgba(0,0,0,0.18);
  }
  .card-front { left: 50px; background: var(--card-white); }
  .card-back { left: 630px; }
  .brand {
    position: absolute;
    right: 34px;
    top: 42px;
    text-align: right;
  }
  .brand-name {
    font-family: "Didact Gothic", sans-serif;
    font-size: 42px;
    line-height: 1;
    color: var(--brand-blue);
    letter-spacing: 0.5px;
  }
  .brand-tagline {
    font-family: "Cinzel", serif;
    font-size: 11px;
    letter-spacing: 7px;
    color: var(--text-grey);
    margin-top: 6px;
    margin-right: -7px;
  }
  .contact {
    position: absolute;
    left: 34px;
    bottom: 30px;
    color: var(--text-dark);
    font-size: 13.5px;
    line-height: 1.55;
  }
  .person-name {
    font-weight: 700;
    font-size: 21px;
    color: var(--brand-blue);
    line-height: 1.2;
  }
  .person-role { margin-bottom: 8px; }
  .contact-line { display: flex; align-items: center; gap: 7px; }
  .contact-line svg { width: 11px; height: 11px; flex: none; }
  .photo {
    width: 100%;
    height: 100%;
    background: linear-gradient(180deg, var(--photo-sky) 0%, #a9c7ea 30%, var(--photo-stone) 55%, #b9a77c 80%, var(--photo-grass) 100%);
  }
</style>
</head>
<body>
  <section class="card card-front">
    <div class="brand">
      <div class="brand-name">Willowmere Loft</div>
      <div class="brand-tagline">BED &amp; BREAKFAST</div>
    </div>
    <div class="contact">
      <div class="person-name">Edward Hollins</div>
      <div class="person-role">Managing Director</div>
      <div class="contact-line">
        <svg viewBox="0 0 12 12" aria-hidden="true"><path d="M2.5 1 L4.5 1 L5.3 3.4 L4 4.4 C4.6 5.8 6 7.3 7.6 8 L8.6 6.7 L11 7.5 L11 9.5 C11 10.3 10.3 11 9.5 11 C5 11 1 7 1 2.5 C1 1.7 1.7 1 2.5 1 Z" fill="var(--brand-blue)"/></svg>
        <span>01632 960418</span>
      </div>
      <div class="contact-line">
        <svg viewBox="0 0 12 12" aria-hidden="true"><circle cx="6" cy="6" r="5.5" fill="var(--brand-blue)"/><path d="M1 6 H11 M6 0.5 C3.5 3 3.5 9 6 11.5 M6 0.5 C8.5 3 8.5 9 6 11.5" stroke="#fff" stroke-width="0.8" fill="none"/></svg>
        <span>www.willowmereloft.co.uk</span>
      </div>
      <div class="contact-address">Brackleford, Hensworth, Somerset, TA14 7QP</div>
    </div>
  </section>
  <section class="card card-back">
    <div class="photo" role="img" aria-label="Photograph of the stone barn guesthouse with red tiled roof, arched window and flower beds under a blue cloudy sky"></div>
  </section>
</body>
</html>
```